Highly rated moving company needs postcard design

We need a highly converting postcard to send when people put their homes for sale online. This should highlight the fact that we're Austin's highest rated moving company, and should convey quality and value. We do local, statewide and long distance moves. We also do office and commerical moves and storage. final design must be sized to work with our mailing system. Please see attached file for more information.

```html
<!DOCTYPE html>
<html lang="en">
<head>
<meta charset="utf-8">
<title>Lakeline Relocation Postcard</title>
<link rel="stylesheet" href="https://fonts.googleapis.com/css2?family=League+Gothic&family=Montserrat:wght@500;600;700&display=swap">
<style>
  :root {
    --board: #3a3a3c;
    --paper: #ffffff;
    --brand-red: #e31e2b;
    --deep-red: #c81b26;
    --navy: #2a2a6c;
    --ink: #111111;
    --ghost: #f3f3f4;
    --ghost-text: #e9e9ea;
  }
  * { margin: 0; padding: 0; box-sizing: border-box; }
  html, body { width: 921px; height: 1200px; overflow: hidden; background: var(--board); }
  body { position: relative; font-family: "Montserrat", sans-serif; }

  .card { position: absolute; left: 84px; width: 752px; height: 501px; background: var(--paper); overflow: hidden; }
  .card--front { top: 81px; }
  .card--back { top: 620px; }

  .brand { position: absolute; left: 30px; top: 50px; font-family: "Montserrat", sans-serif; font-weight: 700; color: var(--navy); font-size: 24px; letter-spacing: 0.5px; line-height: 28px; white-space: nowrap; }

  .photo { position: absolute; }
  .photo--family { left: 464px; top: 123px; width: 288px; height: 278px; background: linear-gradient(135deg, #e9d6cc 0%, #c79a80 55%, #a9735a 100%); }
  .photo--mover { left: 313px; top: 48px; width: 250px; height: 453px; background: linear-gradient(180deg, #d3b894 0%, #c9a37d 25%, #2f8fcf 45%, #1e7dc0 100%); border-radius: 60px 60px 0 0; }

  .hero-band { position: absolute; left: 0; top: 123px; width: 343px; height: 278px; background: linear-gradient(90deg, var(--brand-red), var(--deep-red)); }
  .headline { position: absolute; left: 30px; top: 140px; font-family: "League Gothic", sans-serif; font-weight: 400; color: #fff; font-size: 60px; line-height: 54px; }

  .claim { position: absolute; left: 0; top: 258px; width: 297px; height: 54px; }
  .claim__text { position: absolute; left: 30px; top: 263px; color: #fff; font-weight: 600; font-size: 13px; line-height: 14px; }

  .services__title { position: absolute; left: 30px; top: 315px; font-family: "League Gothic", sans-serif; color: #fff; font-size: 27px; line-height: 28px; }
  .services__list { position: absolute; left: 30px; top: 346px; width: 300px; list-style: none; display: grid; grid-template-columns: 119px 1fr; row-gap: 3px; color: #fff; font-weight: 600; font-size: 11px; }
  .services__list li { display: flex; align-items: center; gap: 3px; }
  .services__list svg { width: 10px; height: 10px; }

  .cta { position: absolute; left: 30px; }
  .cta__label { font-family: "League Gothic", sans-serif; color: var(--brand-red); font-size: 27px; line-height: 28px; }
  .cta__phone { font-weight: 700; color: var(--ink); font-size: 36px; line-height: 42px; }
  .card--front .cta { top: 412px; }
  .card--back .cta { top: 401px; }
  .cta__web { font-weight: 600; color: var(--ink); font-size: 13px; margin-top: 2px; }

  .badges { position: absolute; left: 543px; top: 415px; display: flex; gap: 16px; }
  .badge { height: 28px; border-radius: 3px; }
  .badge--rating { width: 86px; background: #f1f1f1; }
  .badge--stars { width: 84px; background: var(--brand-red); }
  .front-web { position: absolute; right: 23px; top: 456px; font-weight: 600; font-size: 13px; color: var(--ink); }

  .back-panel { position: absolute; left: 0; top: 114px; width: 416px; height: 277px; }
  .back-panel__lead { position: absolute; left: 30px; top: 132px; color: #fff; font-weight: 500; font-size: 20px; line-height: 22px; }
  .back-panel__rule { position: absolute; left: 30px; top: 211px; width: 261px; height: 3px; background: #fff; }
  .back-panel__big { position: absolute; left: 30px; top: 222px; color: #fff; font-weight: 700; font-size: 35px; line-height: 35px; }

  .stamp { position: absolute; left: 637px; top: 26px; width: 94px; height: 94px; border: 1.5px solid var(--ink); }
  .address-line { position: absolute; left: 529px; width: 200px; height: 1px; background: var(--ink); }
  .address-zone { position: absolute; left: 0; top: 0; width: 752px; height: 501px; }
  .address-hint { position: absolute; left: 450px; top: 380px; width: 290px; text-align: center; color: var(--ghost-text); font-weight: 600; font-size: 50px; line-height: 54px; }
</style>
</head>
<body>

<section class="card card--front">
  <p class="brand">Lakeline Relocation</p>

  <div class="photo photo--family" role="img" aria-label="Family unpacking moving boxes, child sitting in a box"></div>
  <div class="hero-band" role="img" aria-label="Red-tinted photo of movers carrying boxes"></div>
  <div class="photo photo--mover" role="img" aria-label="Smiling mover in blue cap and shirt carrying a box, giving a thumbs up"></div>

  <h1 class="headline">LET OUR FAMILY<br>MOVE YOURS</h1>

  <svg class="claim" viewBox="0 0 297 54" preserveAspectRatio="none"><polygon points="0,0 297,0 285,54 0,54" fill="var(--navy)"/></svg>
  <p class="claim__text">WE'RE AUSTIN'S HIGHEST RATED<br>MOVING COMPANY, AND SHOULD<br>CONVEY QUALITY AND VALUE</p>

  <h2 class="services__title">SERVICES</h2>
  <ul class="services__list">
    <li><svg viewBox="0 0 10 10"><circle cx="5" cy="5" r="4" fill="none" stroke="#fff" stroke-width="1.2"/><path d="M3 5l1.5 1.5L8 2.5" fill="none" stroke="#fff" stroke-width="1.3"/></svg>LOCAL MOVES</li>
    <li><svg viewBox="0 0 10 10"><circle cx="5" cy="5" r="4" fill="none" stroke="#fff" stroke-width="1.2"/><path d="M3 5l1.5 1.5L8 2.5" fill="none" stroke="#fff" stroke-width="1.3"/></svg>COMMERCIAL</li>
    <li><svg viewBox="0 0 10 10"><circle cx="5" cy="5" r="4" fill="none" stroke="#fff" stroke-width="1.2"/><path d="M3 5l1.5 1.5L8 2.5" fill="none" stroke="#fff" stroke-width="1.3"/></svg>LONG DISTANCE</li>
    <li><svg viewBox="0 0 10 10"><circle cx="5" cy="5" r="4" fill="none" stroke="#fff" stroke-width="1.2"/><path d="M3 5l1.5 1.5L8 2.5" fill="none" stroke="#fff" stroke-width="1.3"/></svg>PACKING SERVICES</li>
    <li><svg viewBox="0 0 10 10"><circle cx="5" cy="5" r="4" fill="none" stroke="#fff" stroke-width="1.2"/><path d="M3 5l1.5 1.5L8 2.5" fill="none" stroke="#fff" stroke-width="1.3"/></svg>RESIDENTIAL</li>
  </ul>

  <div class="cta">
    <p class="cta__label">GET A FREE QUOTE</p>
    <p class="cta__phone">(512) 555 0142</p>
  </div>

  <div class="badges">
    <span class="badge badge--rating"></span>
    <span class="badge badge--stars"></span>
  </div>
  <p class="front-web">www.lakelinerelocation.com</p>
</section>

<section class="card card--back">
  <p class="brand">Lakeline Relocation</p>

  <svg class="address-zone" viewBox="0 0 752 501"><polygon points="439,283 752,283 752,501 370,501" fill="var(--ghost)"/></svg>
  <p class="address-hint">INSERT<br>ADDRESS</p>

  <svg class="back-panel" viewBox="0 0 416 277" role="img" aria-label="Red-tinted photo of movers packing an office">
    <defs><linearGradient id="panelRed" x1="0" x2="1"><stop offset="0" stop-color="#e31e2b"/><stop offset="1" stop-color="#c81b26"/></linearGradient></defs>
    <polygon points="0,0 416,0 332,277 0,277" fill="url(#panelRed)"/>
  </svg>
  <p class="back-panel__lead">LOCAL STATEWIDE<br>AND LONG DISTANCE<br>MOVES</p>
  <div class="back-panel__rule"></div>
  <p class="back-panel__big">OFFICE AND<br>COMMERICAL<br>MOVES AND<br>STORAGE.</p>

  <div class="stamp"></div>
  <div class="address-line" style="top:176px"></div>
  <div class="address-line" style="top:210px"></div>
  <div class="address-line" style="top:243px"></div>

  <div class="cta">
    <p class="cta__label">GET A FREE QUOTE</p>
    <p class="cta__phone">(512) 555 0142</p>
    <p class="cta__web">www.lakelinerelocation.com</p>
  </div>
</section>

</body>
</html>
```